Invoice design

Please design an invoice like the attached

- Please include a logo in the header (any logo rectangular is fine)

- We do not need a DUE DATE on the invoice (next to the total inc. vat)

- For each product put in smaller text beneath which might contain additional information about the product (e.g. size, colour choices)

- Do not put a signature in the footer

```html
<!DOCTYPE html>
<html lang="en">
<head>
<meta charset="utf-8">
<title>Invoice</title>
<link href="https://fonts.googleapis.com/css2?family=Jost:wght@400;500;600;700&display=swap" rel="stylesheet">
<style>
  :root {
    --brand-red: #e31d35;
    --ink: #161616;
    --logo-ink: #3b3b3b;
    --footer-grey: #e6e6e6;
    --paper: #fdfdfd;
    --white: #ffffff;
  }
  * { margin: 0; padding: 0; box-sizing: border-box; }
  html, body { width: 1200px; height: 1200px; overflow: hidden; background: var(--paper); }
  body { font-family: "Jost", "Futura", sans-serif; color: var(--ink); }
  .canvas { position: relative; width: 1200px; height: 1200px; }
  .abs { position: absolute; line-height: 1; transform: translateY(-50%); white-space: nowrap; }
  .r { text-align: right; }
  .c { transform: translate(-50%, -50%); }

  .header-band { position: absolute; left: 0; top: 0; }

  .brand-mark { position: absolute; left: 712px; top: 206px; width: 36px; height: 36px; background: var(--brand-red); }
  .brand-name { left: 760px; top: 224px; font-size: 24px; font-weight: 600; letter-spacing: 2px; color: var(--logo-ink); }

  .title-arrow { position: absolute; left: 303px; top: 270px; }
  .doc-title { left: 329px; top: 280px; font-size: 41px; font-weight: 500; letter-spacing: -0.5px; }

  .label { font-size: 11.5px; color: var(--brand-red); }
  .meta-value { font-size: 11px; letter-spacing: 1px; font-weight: 500; }
  .party-line { font-size: 10.5px; }
  .party-name { font-weight: 500; }

  .party-divider { position: absolute; left: 637px; top: 320px; width: 1.5px; height: 116px; background: var(--brand-red); }

  .th { font-size: 11.5px; color: var(--brand-red); }
  .th-stack { transform: translateY(-50%); line-height: 1.2; }
  .rule { position: absolute; left: 330px; width: 548px; background: var(--brand-red); }
  .rule-head { top: 506px; height: 2px; }
  .rule-foot { top: 693.5px; height: 1px; }

  .td { font-size: 10.5px; }
  .td-desc { font-size: 8.5px; font-weight: 500; }

  .sum-label { font-size: 10px; color: var(--brand-red); }
  .sum-value { font-size: 13px; }
  .sum-rule { position: absolute; left: 626px; width: 252px; height: 1px; background: var(--brand-red); }
  .grand-box { position: absolute; left: 619px; top: 830px; width: 260px; height: 50px; border: 1.5px dotted var(--brand-red); }
  .grand-value { font-size: 18px; font-weight: 700; }

  .footer-info { position: absolute; left: 270px; top: 924px; width: 438px; height: 150px; background: var(--footer-grey); }
  .footer-pay { position: absolute; left: 708px; top: 924px; width: 228px; height: 150px; background: var(--brand-red); }
  .footer-line { font-size: 10px; }
  .footer-key { font-weight: 500; }
  .pay-divider { position: absolute; left: 745px; top: 944px; width: 1px; height: 108px; background: var(--white); }
  .pay-label { font-size: 11px; color: var(--white); }
  .pay-value { font-size: 10px; color: var(--white); letter-spacing: 1px; }
</style>
</head>
<body>
<main class="canvas">
  <svg class="header-band" width="1200" height="200" aria-hidden="true">
    <polygon points="270.6,133 935.6,133 270.6,190.6" fill="var(--brand-red)"/>
  </svg>

  <div class="brand-mark"></div>
  <div class="abs brand-name">NORTHVALE</div>

  <svg class="title-arrow" width="22" height="24" aria-hidden="true">
    <polygon points="0,0 21,11.5 0,23" fill="var(--brand-red)"/>
  </svg>
  <h1 class="abs doc-title">INVOICE</h1>

  <section class="invoice-meta">
    <div class="abs label" style="left:331px;top:327px">INVOICE:</div>
    <div class="abs meta-value" style="left:331px;top:343px">00001</div>
    <div class="abs label" style="left:331px;top:366px">ISSUE DATE:</div>
    <div class="abs meta-value" style="left:331px;top:383px">July 3, 2024</div>
    <div class="abs label" style="left:331px;top:407px">DELIVERY DATE:</div>
    <div class="abs meta-value" style="left:331px;top:424px">July 3, 2024</div>
  </section>

  <section class="supplier">
    <div class="abs label" style="left:497px;top:327px">SUPPLIER</div>
    <div class="abs party-line party-name" style="left:497px;top:342.5px">Name Ltd</div>
    <div class="abs party-line" style="left:497px;top:357px">Address 01</div>
    <div class="abs party-line" style="left:497px;top:371px">City</div>
    <div class="abs party-line" style="left:497px;top:386px">Zip Code: 0000 000</div>
    <div class="abs party-line" style="left:497px;top:400px">Country</div>
    <div class="abs party-line" style="left:497px;top:415px">VAT No: Aa0000000000</div>
  </section>

  <div class="party-divider"></div>

  <section class="client">
    <div class="abs label" style="left:667px;top:327px">CLIENT</div>
    <div class="abs party-line party-name" style="left:667px;top:342.5px">Personal Name / Company Name</div>
    <div class="abs party-line" style="left:667px;top:357px">Address 01</div>
    <div class="abs party-line" style="left:667px;top:371px">City</div>
    <div class="abs party-line" style="left:667px;top:386px">Zip Code: 0000 000</div>
    <div class="abs party-line" style="left:667px;top:400px">Country</div>
    <div class="abs party-line" style="left:667px;top:415px">VAT No: Aa0000000000</div>
  </section>

  <section class="line-items">
    <div class="abs th" style="left:330px;top:491px">Item</div>
    <div class="abs th" style="left:496px;top:491px">Description</div>
    <div class="abs th r" style="right:474px;top:491px">Quantity</div>
    <div class="abs th th-stack r" style="right:413px;top:484px">Unit Price<br>incl. VAT</div>
    <div class="abs th r" style="right:375px;top:491px">VAT</div>
    <div class="abs th r" style="right:322.5px;top:491px">Total</div>
    <div class="rule rule-head"></div>

    <div class="abs td" style="left:330px;top:526px">Product 01</div>
    <div class="abs td-desc" style="left:497px;top:526px">Size, Colour choices, Packing</div>
    <div class="abs td c" style="left:705.6px;top:526px">2</div>
    <div class="abs td r" style="right:413px;top:526px">15.00</div>
    <div class="abs td c" style="left:815px;top:526px">20%</div>
    <div class="abs td r" style="right:322.5px;top:526px">£30.00</div>

    <div class="abs td" style="left:330px;top:561px">Product 02</div>
    <div class="abs td-desc" style="left:497px;top:561px">Size, Colour choices, Packing</div>
    <div class="abs td c" style="left:705.6px;top:561px">2</div>
    <div class="abs td r" style="right:413px;top:561px">65.00</div>
    <div class="abs td c" style="left:815px;top:561px">20%</div>
    <div class="abs td r" style="right:322.5px;top:561px">£195.00</div>

    <div class="abs td" style="left:330px;top:598px">Product 03</div>
    <div class="abs td-desc" style="left:497px;top:598px">Size, Colour choices, Packing</div>
    <div class="abs td c" style="left:705.6px;top:598px">0</div>
    <div class="abs td r" style="right:413px;top:598px">0.00</div>
    <div class="abs td c" style="left:815px;top:598px">20%</div>
    <div class="abs td r" style="right:322.5px;top:598px">£0.00</div>

    <div class="abs td" style="left:330px;top:635px">Product 04</div>
    <div class="abs td-desc" style="left:497px;top:635px">Size, Colour choices, Packing</div>
    <div class="abs td c" style="left:705.6px;top:635px">0</div>
    <div class="abs td r" style="right:413px;top:635px">0.00</div>
    <div class="abs td c" style="left:815px;top:635px">20%</div>
    <div class="abs td r" style="right:322.5px;top:635px">£0.00</div>

    <div class="abs td" style="left:330px;top:672px">Product 05</div>
    <div class="abs td-desc" style="left:497px;top:672px">Size, Colour choices, Packing</div>
    <div class="abs td c" style="left:705.6px;top:672px">0</div>
    <div class="abs td r" style="right:413px;top:672px">0.00</div>
    <div class="abs td c" style="left:815px;top:672px">20%</div>
    <div class="abs td r" style="right:322.5px;top:672px">£0.00</div>

    <div class="rule rule-foot"></div>
  </section>

  <section class="summary">
    <div class="abs sum-label" style="left:626px;top:712px">SUBTOTAL:</div>
    <div class="abs sum-value r" style="right:323px;top:711px">£225.00</div>
    <div class="sum-rule" style="top:729px"></div>
    <div class="abs sum-label" style="left:626px;top:746px">SHIPPING:</div>
    <div class="abs sum-value r" style="right:323px;top:745px">£18.00</div>
    <div class="sum-rule" style="top:763px"></div>
    <div class="abs sum-label" style="left:626px;top:780px">TOTAL EXCL. VAT:</div>
    <div class="abs sum-value r" style="right:323px;top:779px">£205.50</div>
    <div class="sum-rule" style="top:797px"></div>
    <div class="abs sum-label" style="left:626px;top:813px">VAT 20%:</div>
    <div class="abs sum-value r" style="right:323px;top:812px">£37.50</div>
    <div class="grand-box"></div>
    <div class="abs sum-label" style="left:626px;top:854px">TOTAL INCL. VAT:</div>
    <div class="abs grand-value r" style="right:334px;top:853px">£243.00</div>
  </section>

  <footer>
    <div class="footer-info"></div>
    <div class="abs footer-line footer-key" style="left:329px;top:962px">Name Ltd</div>
    <div class="abs footer-line" style="left:329px;top:976px">Address, Country</div>
    <div class="abs footer-line" style="left:329px;top:991px"><span class="footer-key">Phone:</span> +44 0000 000000</div>
    <div class="abs footer-line" style="left:329px;top:1005px"><span class="footer-key">Email:</span> companyname@email.com</div>
    <div class="abs footer-line" style="left:329px;top:1020px"><span class="footer-key">Website:</span> www.companyname.com</div>
    <div class="abs footer-line" style="left:329px;top:1034px"><span class="footer-key">Social Media:</span> @companyname</div>

    <div class="footer-pay"></div>
    <div class="pay-divider"></div>
    <div class="abs pay-label" style="left:757px;top:949px">PAYMENT METHOD</div>
    <div class="abs pay-value" style="left:757px;top:966px">Bank Transfer</div>
    <div class="abs pay-label" style="left:757px;top:991px">BANK ACCOUNT</div>
    <div class="abs pay-value" style="left:757px;top:1008px">0000 0000 0000 0000</div>
    <div class="abs pay-label" style="left:757px;top:1032px">ORDER NUMBER</div>
    <div class="abs pay-value" style="left:757px;top:1049px">#0000</div>
  </footer>
</main>
</body>
</html>
```